Flyer for the Harvest of lanterns conference

Flyer design for an annual international conference called "VELMARK 2017". This is a conference for young adults, so we hope to produce a design that is both professional and appealing to young people in general

We'd like the flyer to showcase the conference brand logo, and clearly highlight the key information to people who will read it.

Target Market(s)

Young people, young adults

Industry/Entity Type

Religious

Font styles to use
Sans Serif

Colors

Designer to choose colors to be used in the design.

Requirements
Must have
• - Should be only one page (Vertical or Horizontal).
• - the VELMAK logo and all the information found in the attached text file. This includes: Main topic: Your sons and daughters shall prophesy,
• Dates and time, location, contact information and everything that is in the attached text file.
Nice to have
• It would be nice to see samples where the white logo is used and another where the black one is used.
Should not have
• This is NOT a folded flyer, we will be sticking it on doors and public places. And we will be printing large simple to put on walls. So only one page with few words like an add (the words are in the attached file)

```html
<!DOCTYPE html>
<html lang="en">
<head>
<meta charset="utf-8">
<title>VELMARK 2017 — Harvest of Lanterns Conference</title>
<link href="https://fonts.googleapis.com/css2?family=Bebas+Neue&family=Montserrat:wght@300;700;800&display=swap" rel="stylesheet">
<style>
:root{
  --ink:#1b1b1b;
  --slate:#454545;
  --white:#ffffff;
  --mist:#dcdcdc;
  --muted:#b9b9b9;
  --red:#e3141f;
  --red-deep:#b3102a;
  --accent:#c8102e;
  --gold:#f2a516;
}
*{margin:0;padding:0;box-sizing:border-box}
html,body{width:927px;height:1200px;overflow:hidden;background:var(--white)}
.flyer{position:relative;width:927px;height:1200px;overflow:hidden;background:var(--white);font-family:"Bebas Neue",sans-serif;color:var(--white)}
.scenery{position:absolute;left:0;top:190px;width:927px;height:1010px;
  background:linear-gradient(180deg,rgba(255,255,255,0) 0%,#a9a9b6 6%,#7d7b90 14%,#3c3c3c 24%,#262626 40%,#3a3a3a 55%,#6e6e6e 64%,#8c5a5c 70%,#d8141f 76%,var(--red) 100%)}
.triangle{position:absolute;left:0;top:0}
.brand-block{position:absolute;left:34px;top:40px;font-family:"Montserrat",sans-serif;color:var(--ink);line-height:1}
.brand-block .edition{font-size:35px;font-weight:800;color:var(--slate);letter-spacing:1px}
.brand-block .name{font-size:27px;font-weight:800;letter-spacing:2px;margin-top:8px;line-height:1.15}
.brand-block .kind{font-size:20px;font-weight:300;letter-spacing:2px;margin-top:2px}
.brand-mark{position:absolute;left:636px;top:48px;width:240px;text-align:center;font-family:"Montserrat",sans-serif}
.brand-mark .dot{width:120px;height:120px;border-radius:50%;background:var(--gold);margin:0 auto 12px}
.brand-mark .word{font-size:44px;font-weight:800;color:var(--ink);letter-spacing:3px}
.headline{position:absolute;left:0;width:927px;text-align:center;line-height:1}
.headline.top{top:292px;font-size:106px;letter-spacing:2px}
.headline.top span{display:block;height:92px}
.rule{position:absolute;left:242px;width:442px;height:4px;background:var(--white)}
.subhead{position:absolute;top:518px;left:0;width:927px;text-align:center;font-size:58px;letter-spacing:3px;line-height:1}
.date{position:absolute;top:620px;left:0;width:927px;text-align:center;font-size:50px;color:var(--mist);letter-spacing:2px;line-height:1}
.venue{position:absolute;top:712px;left:0;width:927px;text-align:center;line-height:1;letter-spacing:1px}
.venue .hall{font-size:38px;margin-bottom:16px}
.venue .line{font-size:29px;margin-bottom:13px}
.speakers{position:absolute;top:928px;left:0;width:927px;text-align:center;color:var(--muted);line-height:1;letter-spacing:1px}
.speakers .label{font-size:25px;margin-bottom:10px}
.speakers .row{font-size:28px;margin-bottom:10px}
.contact-bar{position:absolute;left:72px;top:1096px;width:784px;height:34px;background:var(--white);display:flex;justify-content:center;align-items:center;gap:34px;font-family:"Montserrat",sans-serif;font-weight:700;font-size:21px;color:var(--accent)}
.contact-bar .item{display:flex;align-items:center;gap:8px}
.website{position:absolute;top:1146px;left:0;width:927px;text-align:center;font-size:34px;letter-spacing:6px;line-height:1}
</style>
</head>
<body>
<main class="flyer">
  <div class="scenery" role="img" aria-label="Layered misty mountains and dark pine forest fading into a red field with faint faces"></div>
  <svg class="triangle" width="927" height="600" aria-hidden="true"><polygon points="462,200 290,578 636,578" fill="var(--red-deep)" opacity="0.85"/></svg>

  <header class="brand-block">
    <div class="edition">VELMARK 2017</div>
    <div class="name">HARVEST OF<br>LANTERNS</div>
    <div class="kind">CONFERENCE</div>
  </header>

  <div class="brand-mark">
    <div class="dot"></div>
    <div class="word">VELMAK</div>
  </div>

  <h1 class="headline top"><span>YOUR SONS</span><span>&amp; DAUGHTERS</span></h1>
  <div class="rule" style="top:488px"></div>
  <div class="rule" style="top:496px;height:2px"></div>
  <h2 class="subhead">SHALL PROPHECY</h2>
  <div class="rule" style="top:583px"></div>
  <div class="rule" style="top:598px"></div>

  <p class="date">1 - 2 - 3 SEPTEMBER 2017 | 6:00PM</p>

  <address class="venue" style="font-style:normal">
    <div class="hall">BIRCHLINE HALL</div>
    <div class="line">HARBORVIEW LODGE</div>
    <div class="line">418 ELM CREST AVENUE</div>
    <div class="line">LAKEVIEW, ME 04999 USA</div>
  </address>

  <section class="speakers">
    <div class="label">SPEAKERS INCLUDE:</div>
    <div class="row">● PROPHET MARCEL TONDEAU ● BISHOP SAMUEL ORIWA</div>
    <div class="row">● PROPHET JONAS LEKA MBANZI</div>
    <div class="row">● PROPHET ANDRE KILOLO ● PROPHET PAUL NDEMO</div>
  </section>

  <div class="contact-bar">
    <span class="item"><svg width="20" height="20" viewBox="0 0 20 20" aria-hidden="true"><circle cx="10" cy="10" r="8.5" fill="none" stroke="currentColor" stroke-width="1.5"/><path d="M7 5.5l1.6 2.2-1 1.2c.6 1.2 1.4 2 2.6 2.6l1.2-1 2.2 1.6-.8 1.6c-3.4-.4-6.2-3.2-6.6-6.6z" fill="currentColor"/></svg>+1 (555) 014 2236</span>
    <span class="item"><svg width="22" height="16" viewBox="0 0 22 16" aria-hidden="true"><rect x="1" y="1" width="20" height="14" fill="none" stroke="currentColor" stroke-width="1.6"/><path d="M1 1l10 8 10-8" fill="none" stroke="currentColor" stroke-width="1.6"/></svg>hello@cedarcourt.org</span>
  </div>

  <p class="website">WWW.LANTERNHOUSE.ORG</p>
</main>
</body>
</html>
```